Cat sitting business Web Design Project ***

I have a cat sitting business where I either take care of cats in their home or board them in mine

I need a website which offers my services, my rates, about me, FAQ's, Hours of operation and service areas covered, testimonials, contact info, newsletter sign up, gallery of photos and the ability for me to go in and update when needed.

Coding

Coded - Design and coding required

Number of Pages Required

5+ page

```html
<!DOCTYPE html>
<html lang="en">
<head>
<meta charset="utf-8">
<title>Purrfect Paws Cat Care</title>
<link href="https://fonts.googleapis.com/css2?family=Josefin+Sans:wght@600;700&family=Raleway:ital,wght@0,400;0,500;0,600;0,700;1,400&display=swap" rel="stylesheet">
<style>
:root{
  --maroon:#9b4e52;
  --maroon-dark:#6b3d42;
  --green:#7dbb46;
  --green-deep:#5e9a33;
  --ink:#333;
  --text:#444;
  --soft:#efefef;
  --footer:#222;
  --white:#fff;
}
*{box-sizing:border-box;margin:0;padding:0}
html,body{width:1200px;height:4743px;overflow:hidden}
body{position:relative;font-family:"Raleway",sans-serif;color:var(--text);background:var(--white)}
.abs{position:absolute}
.head-font{font-family:"Josefin Sans",sans-serif;font-weight:700}
.photo{position:absolute}
.btn{position:absolute;display:flex;align-items:center;justify-content:center;border-radius:30px;color:var(--white);font-weight:700;font-family:"Raleway",sans-serif}
.btn-green{background:var(--green)}
.btn-maroon{background:var(--maroon)}
.btn-dark{background:#5a3338}

/* header */
.site-header{position:absolute;left:0;top:0;width:1200px;height:142px;background:var(--white);z-index:3}
.logo{position:absolute;left:68px;top:-10px;width:250px;height:250px;border-radius:50%;background:var(--white);z-index:4;display:flex;flex-direction:column;align-items:center;justify-content:center;gap:8px}
.logo-mark{width:46px;height:46px;border-radius:50%;background:var(--green)}
.logo-name{font-family:"Josefin Sans",sans-serif;font-weight:700;color:var(--maroon);font-size:25px;text-align:center;line-height:1.1}
.call{position:absolute;right:74px;top:28px;font-family:"Josefin Sans",sans-serif;font-weight:700;font-size:24px;color:var(--maroon);display:flex;align-items:center;gap:10px}
.call span{color:var(--green)}
.nav{position:absolute;top:94px;left:0;font-size:17px;font-weight:500;color:var(--ink)}
.nav a{position:absolute;white-space:nowrap;color:inherit;text-decoration:none}
.nav a.active{color:var(--green)}

/* hero */
.hero{position:absolute;left:0;top:142px;width:1200px;height:723px;background:linear-gradient(120deg,#3f6b2a 0%,#6f9a4a 35%,#5a6b78 60%,#37455a 100%)}
.hero-title{position:absolute;left:0;top:265px;width:1200px;text-align:center;color:var(--white);font-size:88px;line-height:86px;text-shadow:0 2px 6px rgba(0,0,0,.35)}
.hero .btn{left:522px;top:489px;width:152px;height:48px;font-size:18px}
.dots{position:absolute;left:492px;top:677px;display:flex;gap:6px}
.dots i{width:52px;height:5px;background:var(--white);display:block}
.dots i.on{background:#555;border:1px solid var(--white)}

/* section headings */
.sec-title{position:absolute;left:0;width:1200px;text-align:center;color:var(--maroon);font-size:58px}

/* services */
.svc-intro{position:absolute;left:70px;top:1027px;width:1060px;text-align:center;font-size:20px;line-height:28px}
.card{position:absolute;background:var(--white);box-shadow:0 2px 12px rgba(0,0,0,.12);text-align:center}
.svc-card{top:1119px;width:244px;height:414px}
.svc-card .photo{left:0;top:0;width:244px;height:190px}
.svc-card h3{position:absolute;top:210px;width:100%;font-family:"Josefin Sans",sans-serif;font-weight:700;font-size:22px;color:#5a3338}
.svc-card p{position:absolute;top:243px;left:14px;right:14px;font-size:14.5px;line-height:23px}
.svc-card .btn{left:67px;top:362px;width:110px;height:34px;font-size:13px}
.deco{position:absolute;top:1551px;height:173px}
.view-all{left:491px;top:1579px;width:216px;height:50px;font-size:18px}

/* about */
.about-photo{position:absolute;left:0;top:1724px;width:637px;height:604px;background:linear-gradient(135deg,#d9c08a,#a88452 55%,#4a3a2e)}
.about-inset{position:absolute;left:0;top:1843px;width:340px;height:373px;border:4px solid var(--white);background:linear-gradient(135deg,#e9e2d8,#b09278 60%,#6a5140)}
.about-panel{position:absolute;left:637px;top:1724px;width:563px;height:604px;background:var(--soft)}
.about-panel h2{position:absolute;left:44px;top:108px;color:var(--maroon);font-size:56px}
.about-panel p{position:absolute;left:44px;top:176px;width:430px;font-size:17px;line-height:29.5px;color:var(--text)}
.about-panel .btn{left:44px;top:443px;width:150px;height:48px;font-size:18px}

/* testimonials */
.testimonials{position:absolute;left:0;top:2328px;width:1200px;height:474px;background:linear-gradient(90deg,var(--maroon-dark),#9c5559)}
.testimonials h2{position:absolute;top:95px;width:100%;text-align:center;color:var(--white);font-size:56px}
.testimonials blockquote{position:absolute;left:185px;top:180px;width:830px;text-align:center;color:#f1e3e3;font-style:italic;font-size:18px;line-height:32.5px}
.testimonials cite{position:absolute;top:337px;width:100%;text-align:center;color:var(--white);font-style:normal;font-weight:700;font-size:19px}
.arrow{position:absolute;top:205px}

/* rates */
.rate-card{top:2944px;width:321px;height:396px}
.rate-card .photo{left:0;top:0;width:321px;height:202px}
.price{position:absolute;left:126px;top:166px;width:68px;height:70px;background:var(--green);color:var(--white)}
.price b{display:block;font-family:"Josefin Sans",sans-serif;font-size:32px;margin-top:10px}
.price small{font-size:11px}
.rate-card h3{position:absolute;top:255px;width:100%;font-size:19px;font-weight:700;color:var(--ink)}
.rate-card p{position:absolute;top:285px;left:14px;right:14px;font-size:15px;line-height:23px}
.rate-card .btn{left:103px;top:380px;width:115px;height:36px;font-size:13px}

/* gallery */
.gallery-bg{position:absolute;left:0;top:3441px;width:1200px;height:739px;background:var(--soft)}
.tile{position:absolute}

/* newsletter */
.newsletter{position:absolute;left:0;top:4180px;width:1200px;height:159px;background:linear-gradient(90deg,#4f8a2c,#7dbb46 45%,#6aa63c)}
.newsletter h2{position:absolute;left:153px;top:62px;color:var(--white);font-size:32px}
.email{position:absolute;left:469px;top:53px;width:585px;height:52px;background:var(--white);border-radius:30px;font-size:16px;color:#555;padding:17px 0 0 30px}
.email i{position:absolute;right:8px;top:8px;width:36px;height:36px;border-radius:50%;background:#4a2c30}

/* footer */
.site-footer{position:absolute;left:0;top:4339px;width:1200px;height:404px;background:var(--footer);color:#ddd;font-size:14px}
.site-footer h4{position:absolute;top:65px;color:var(--white);font-size:18px;font-weight:600}
.col{position:absolute;top:102px;line-height:27.5px}
.contact-row{position:relative;padding-left:41px;margin-bottom:12px;line-height:24px}
.contact-row svg{position:absolute;left:0;top:2px}
.closed{color:var(--green)}
.copy{position:absolute;left:81px;top:348px}
.social{position:absolute;left:996px;top:345px;display:flex;gap:19px}
.social i{width:22px;height:22px;border-radius:50%;background:var(--white);display:block}
</style>
</head>
<body>

<header class="site-header">
  <div class="call">
    <svg width="24" height="24" viewBox="0 0 24 24"><circle cx="12" cy="12" r="12" fill="#9b4e52"/><path d="M8 6l3 3-1.5 1.5c.8 1.7 2.2 3.1 4 4L15 13l3 3-2 2c-5 0-10-5-10-10z" fill="#fff"/></svg>
    Call Us: <span>555 210 3846</span>
  </div>
  <nav class="nav">
    <a class="active" style="left:412px">Home</a>
    <a style="left:499px">About Me</a>
    <a style="left:618px">Services</a>
    <a style="left:721px">Gallery</a>
    <a style="left:817px">FAQs</a>
    <a style="left:896px">Testimonials</a>
    <a style="left:1032px">Contact Us</a>
  </nav>
</header>
<div class="logo">
  <div class="logo-mark"></div>
  <div class="logo-name">Purrfect Paws<br>Cat Care</div>
</div>

<section class="hero" role="img" aria-label="Smiling woman holding a grey cat in a leafy garden">
  <h1 class="hero-title head-font">Welcome to<br>Purrfect Paws Cat Care</h1>
  <a class="btn btn-green">Read More</a>
  <div class="dots"><i></i><i></i><i class="on"></i><i></i></div>
  <svg class="abs" style="left:0;top:643px" width="1200" height="80" viewBox="0 0 1200 80" preserveAspectRatio="none">
    <path d="M0 45 C200 10 420 10 620 40 C820 70 1000 60 1200 20 L1200 80 L0 80Z" fill="#7dbb46"/>
    <path d="M0 58 C200 22 420 22 620 50 C820 78 1000 72 1200 34 L1200 80 L0 80Z" fill="#fff"/>
  </svg>
</section>

<h2 class="sec-title head-font" style="top:952px">Services Offer</h2>
<p class="svc-intro">Sed ut perspiciatis unde omnis iste natus error sit voluptatem accusantium doloremque laudantium, totam rem aperiam, eaque ipsa quae ab illo inventore veritatis et quasi architecto.</p>

<article class="card svc-card" style="left:74px">
  <div class="photo" role="img" aria-label="Cat having its claws trimmed" style="background:linear-gradient(135deg,#8a8078,#5d5a5e)"></div>
  <h3>Voluptatem Quia</h3>
  <p>Sed ut perspiciatis unde omnis iste natus error sit voluptatem accusantium doloremque ullamco laboris nisi.</p>
  <a class="btn btn-maroon">Read More</a>
</article>
<article class="card svc-card" style="left:342px">
  <div class="photo" role="img" aria-label="Black and white cat being bathed" style="background:linear-gradient(135deg,#b9bdc0,#3c3f44)"></div>
  <h3>Voluptatem Quia</h3>
  <p>Sed ut perspiciatis unde omnis iste natus error sit voluptatem accusantium doloremque ullamco laboris nisi.</p>
  <a class="btn btn-green">Read More</a>
</article>
<article class="card svc-card" style="left:611px">
  <div class="photo" role="img" aria-label="Cat eating from a feeding mat" style="background:linear-gradient(135deg,#e5ddd3,#b9a28a)"></div>
  <h3>Voluptatem Quia</h3>
  <p>Sed ut perspiciatis unde omnis iste natus error sit voluptatem accusantium doloremque ullamco laboris nisi.</p>
  <a class="btn btn-green">Read More</a>
</article>
<article class="card svc-card" style="left:880px">
  <div class="photo" role="img" aria-label="Tabby cat playing with a hand" style="background:linear-gradient(135deg,#dde6ec,#b48a5e)"></div>
  <h3>Voluptatem Quia</h3>
  <p>Sed ut perspiciatis unde omnis iste natus error sit voluptatem accusantium doloremque ullamco laboris nisi.</p>
  <a class="btn btn-green">Read More</a>
</article>

<div class="deco" role="img" aria-label="Grey fluffy cat sitting" style="left:0;width:184px;background:linear-gradient(180deg,#fff,#8a8c92 60%,#5d5f66)"></div>
<div class="deco" role="img" aria-label="Ginger kitten" style="left:972px;width:228px;background:linear-gradient(180deg,#f4f4f4,#e0a36a 60%,#c9824a)"></div>
<a class="btn btn-dark view-all">View All Services</a>

<div class="about-photo" role="img" aria-label="Older woman cuddling a white cat on a sofa"></div>
<div class="about-inset" role="img" aria-label="Woman holding a tabby cat by a window"></div>
<section class="about-panel">
  <h2 class="head-font">About Me</h2>
  <p>Sed ut perspiciatis unde omnis iste natus error sit voluptatem accusantium doloremque laudantium, totam rem aperiam, eaque ipsa quae ab illo inventore veritatis et quasi architecto beatae vitae dicta sunt explicabo. Nemo enim ipsam voluptatem quia voluptas sit aspernatur aut odit aut fugit, sed quia consequuntur magni dolores eos qui ratione voluptatem porro quisquam est, qui dolorem.</p>
  <a class="btn btn-green">Read More</a>
</section>

<section class="testimonials">
  <h2 class="head-font">Testimonials</h2>
  <svg class="arrow" style="left:135px" width="34" height="64"><path d="M32 2 L3 32 L32 62" stroke="#c49093" stroke-width="2" fill="none"/></svg>
  <svg class="arrow" style="left:1031px" width="34" height="64"><path d="M2 2 L31 32 L2 62" stroke="#c49093" stroke-width="2" fill="none"/></svg>
  <blockquote>Sed ut perspiciatis unde omnis iste natus error sit voluptatem accusantium doloremque laudantium, totam rem aperiam, eaque ipsa quae ab illo inventore veritatis et quasi architecto beatae vitae dicta sunt explicabo. Nemo enim ipsam voluptatem quia voluptas sit aspernatur aut odit aut fugit, sed quia consequuntur magni dolores eos qui ratione voluptatem sequi nesciunt..</blockquote>
  <cite>Margaret, Ashford</cite>
</section>

<h2 class="sec-title head-font" style="top:2855px">My Rates</h2>
<article class="card rate-card" style="left:75px">
  <div class="photo" role="img" aria-label="Calico cat being stroked on a table" style="background:linear-gradient(135deg,#f2f2f2,#9a8a7a)"></div>
  <div class="price"><b>$8</b><small>Per Visit</small></div>
  <h3>Pellentesque Fauc</h3>
  <p>At vero eos et accusamus et iusto odioi gnis simos ducimus qui blanditiis praesen iulorm voluptatum deleniti atque</p>
  <a class="btn btn-maroon">Read More</a>
</article>
<article class="card rate-card" style="left:440px">
  <div class="photo" role="img" aria-label="Grey tabby cat playing on its back" style="background:linear-gradient(135deg,#e8e8e8,#7d7d80)"></div>
  <div class="price"><b>$8</b><small>Per Visit</small></div>
  <h3>Pellentesque Fauc</h3>
  <p>At vero eos et accusamus et iusto odioi gnis simos ducimus qui blanditiis praesen iulorm voluptatum deleniti atque</p>
  <a class="btn btn-maroon">Read More</a>
</article>
<article class="card rate-card" style="left:804px">
  <div class="photo" role="img" aria-label="Woman hugging a ginger cat" style="background:linear-gradient(135deg,#c9753e,#efe6dc)"></div>
  <div class="price"><b>$8</b><small>Per Visit</small></div>
  <h3>Pellentesque Fauc</h3>
  <p>At vero eos et accusamus et iusto odioi gnis simos ducimus qui blanditiis praesen iulorm voluptatum deleniti atque</p>
  <a class="btn btn-maroon">Read More</a>
</article>

<div class="gallery-bg"></div>
<svg class="abs" style="left:0;top:3430px" width="1200" height="60" viewBox="0 0 1200 60" preserveAspectRatio="none">
  <path d="M0 40 C250 60 450 30 700 22 C900 16 1050 18 1200 0 L1200 60 L0 60Z" fill="#7dbb46"/>
  <path d="M0 50 C250 66 450 38 700 30 C900 24 1050 26 1200 8 L1200 60 L0 60Z" fill="#efefef"/>
</svg>
<h2 class="sec-title head-font" style="top:3550px">Photo Gallery</h2>
<div class="tile" role="img" aria-label="Ginger cat having its eyes cleaned" style="left:74px;top:3654px;width:340px;height:273px;background:linear-gradient(135deg,#2f3a4a,#d08a4e)"></div>
<div class="tile" role="img" aria-label="Woman cuddling a tabby cat" style="left:74px;top:3943px;width:340px;height:179px;background:linear-gradient(135deg,#eeeae4,#a28a70)"></div>
<div class="tile" role="img" aria-label="Cat receiving medicine drops" style="left:431px;top:3654px;width:340px;height:181px;background:linear-gradient(135deg,#f0f0f0,#3c3c3c)"></div>
<div class="tile" role="img" aria-label="Calico cat eating from a bowl" style="left:431px;top:3851px;width:340px;height:271px;background:linear-gradient(135deg,#7a5a3e,#2e2a2a)"></div>
<div class="tile" role="img" aria-label="Cat being washed under a shower" style="left:786px;top:3654px;width:340px;height:273px;background:linear-gradient(135deg,#c9ccce,#3a3d42)"></div>
<div class="tile" role="img" aria-label="Woman holding a cat at sunset" style="left:786px;top:3943px;width:340px;height:179px;background:linear-gradient(135deg,#f3e6d2,#9a6a44)"></div>

<section class="newsletter">
  <h2 class="head-font">Newsletter Sign up</h2>
  <div class="email">Email:<i><svg width="36" height="36"><path d="M15 12l8 6-8 6z" fill="#fff"/></svg></i></div>
</section>

<footer class="site-footer">
  <h4 style="left:83px">Contact Info</h4>
  <h4 style="left:410px">About Us</h4>
  <h4 style="left:673px">Services</h4>
  <h4 style="left:957px">Hours</h4>
  <div class="col" style="left:80px;width:300px">
    <div class="contact-row"><svg width="22" height="26" viewBox="0 0 22 26"><path d="M11 24C5 16 3 12 3 9a8 8 0 0116 0c0 3-2 7-8 15z" stroke="#7dbb46" stroke-width="1.8" fill="none"/><circle cx="11" cy="9" r="3" stroke="#7dbb46" stroke-width="1.8" fill="none"/></svg>Whisker Lane Studio<br>Ashford, UK</div>
    <div class="contact-row"><svg width="26" height="24" viewBox="0 0 26 24"><path d="M6 2l4 4-2 2c1 3 4 6 7 7l2-2 4 4-3 3C10 20 4 14 3 5z" stroke="#7dbb46" stroke-width="1.8" fill="none"/></svg>Phone: 555-210-3846</div>
    <div class="contact-row"><svg width="28" height="20" viewBox="0 0 28 20"><rect x="1" y="2" width="26" height="16" stroke="#7dbb46" stroke-width="1.8" fill="none"/><path d="M1 2l13 9 13-9" stroke="#7dbb46" stroke-width="1.8" fill="none"/></svg>hello@purrfectpaws.example</div>
  </div>
  <div class="col" style="left:410px">Home<br>About Me<br>Services<br>Gallery<br>FAQS<br>Testimonials<br>Contact Us</div>
  <div class="col" style="left:673px">Lorem ipsum dolo<br>Consectetur adipiscing elit<br>Fusce eec consequat<br>Praesent elementum<br>Jmauris posuer</div>
  <div class="col" style="left:957px">Mon - Fri &nbsp; 10:00 am - 6:00pm<br>Mon - Fri &nbsp; 10:00 am - 6:00pm<br>Sunday &nbsp;&nbsp;&nbsp; <span class="closed">Closed</span></div>
  <div class="copy">Copyright 2022 All Rights Reserved</div>
  <div class="social"><i></i><i></i><i></i><i></i></div>
</footer>

</body>
</html>
```